Etiketten für Flaschen
Zielgruppe
Wir sind Getränkehersteller- und händler. Für unsere Partner haben wir exklusive Eigenmarken, die nur unserer Partner verkaufen. Das 'mirel' Wasser ist eine exklusive Gastronomiemarke, die nicht im Handel erhältlich ist.
Unsere Gourmetlinie von mirel besteht aus einem Mineralwasser Naturelle und Feinperlig, in der 0,75l und 0,2l Glas Flasche.
Aufgabenstellung
Wir möchten für unsere Wasser Flaschen gerne eine Serie mit Sonderetiketten designen lassen.
Diese sollen einen 'künstlerischen' Effekt haben.
Wichtig:
Die Flasche an sich bleibt unverändert, das Etikettenformat bleibt bestehen.
Alle heutigen Schriftzüge dürfen in Größe und Position nicht verändert werden, auch der farbige Balken in rot bzw. blau muss bestehen bleiben. Wir suchen somit lediglich eine neue Gestaltung für den aktuell weißen Hintergrund bzw. die weißen Etikettenflächen.
Bitte gestalten Sie zunächst nur das Etikett der 0,75l Flasche, egal ob für Naturelle oder Feinperlig.

```html
<!DOCTYPE html>
<html lang="de">
<head>
<meta charset="utf-8">
<title>mirel – Etiketten Gastro Gourmet Linie</title>
<link href="https://fonts.googleapis.com/css2?family=Barlow:wght@300;400;500;700&display=swap" rel="stylesheet">
<style>
  :root {
    --page-bg: #ffffff;
    --blue-dark: #1c4690;
    --blue-mid: #2d82e2;
    --blue-deep: #1b3c7c;
    --blue-wash-top: #f6f7fc;
    --blue-wash-mid: #b4c2ee;
    --blue-wash-low: #6f9ae0;
    --red-dark: #971b37;
    --red-mid: #e53261;
    --red-deep: #821a30;
    --red-wash-top: #fff6f6;
    --red-wash-mid: #f2b7b9;
    --red-wash-low: #e0566a;
    --white: #ffffff;
  }
  * { margin: 0; padding: 0; box-sizing: border-box; }
  html, body {
    width: 1200px;
    height: 614px;
    overflow: hidden;
    background: var(--page-bg);
  }
  .canvas {
    position: relative;
    width: 1200px;
    height: 614px;
    font-family: "Barlow", "Helvetica Neue", Arial, sans-serif;
  }
  .label {
    position: absolute;
    top: 193px;
    width: 360px;
    height: 260px;
    overflow: hidden;
    box-shadow: 6px 8px 14px rgba(0, 0, 0, 0.18);
  }
  .label--feinperlig { left: 204.5px; }
  .label--naturelle { left: 612.5px; }

  .label__artwork {
    position: absolute;
    inset: 0;
  }
  .label--feinperlig .label__artwork {
    background: linear-gradient(180deg, var(--blue-wash-top) 0%, #eef1fb 28%, var(--blue-wash-mid) 55%, var(--blue-wash-low) 80%, #4f8ad6 100%);
  }
  .label--naturelle .label__artwork {
    background: linear-gradient(180deg, var(--red-wash-top) 0%, #fcecec 28%, var(--red-wash-mid) 55%, var(--red-wash-low) 82%, #d63d58 100%);
  }

  .label__top-bar {
    position: absolute;
    left: 0; top: 0;
    width: 100%;
    height: 19px;
  }
  .label--feinperlig .label__top-bar,
  .label--feinperlig .label__bottom-bar {
    background: linear-gradient(90deg, var(--blue-dark) 0%, var(--blue-dark) 15%, var(--blue-mid) 40%, #2a6fcc 62%, var(--blue-deep) 78%, #2152a0 100%);
  }
  .label--naturelle .label__top-bar,
  .label--naturelle .label__bottom-bar {
    background: linear-gradient(90deg, var(--red-dark) 0%, var(--red-dark) 18%, var(--red-mid) 48%, #cf2b55 64%, var(--red-deep) 78%, #a31f40 100%);
  }

  .label__bottom-bar {
    position: absolute;
    left: 0; bottom: 0;
    width: 100%;
    height: 37px;
    border-radius: 60% 60% 0 0 / 3px 3px 0 0;
    display: flex;
    align-items: center;
    justify-content: center;
  }
  .label__line {
    color: var(--white);
    font-size: 15.5px;
    letter-spacing: 1.6px;
    font-weight: 300;
    white-space: nowrap;
    padding-top: 1px;
  }
  .label__line strong { font-weight: 700; letter-spacing: 1.4px; }

  .label__brand {
    position: absolute;
    left: 0; top: 60px;
    width: 100%;
    text-align: center;
    font-size: 92px;
    font-weight: 400;
    line-height: 1;
    letter-spacing: 1px;
  }
  .label--feinperlig .label__brand { color: #2a62be; }
  .label--naturelle .label__brand { color: #b42246; }

  .label__variant {
    position: absolute;
    left: 0; top: 160px;
    width: 100%;
    text-align: center;
    color: var(--white);
    font-size: 22px;
    font-weight: 500;
    letter-spacing: 2px;
    line-height: 1;
  }
  .label__description {
    position: absolute;
    left: 0; top: 190px;
    width: 100%;
    text-align: center;
    color: var(--white);
    font-size: 13px;
    font-weight: 400;
    letter-spacing: 0.5px;
    line-height: 1;
  }
</style>
</head>
<body>
<main class="canvas">
  <section class="label label--feinperlig">
    <div class="label__artwork" role="img" aria-label="Künstlerischer Hintergrund mit feinen, hellen Zweig- und Wasserlinien auf blauem Verlauf"></div>
    <div class="label__top-bar"></div>
    <div class="label__brand">mirel</div>
    <div class="label__variant">FEINPERLIG</div>
    <p class="label__description">Natürliches Mineralwasser mit Kohlensäure versetzt</p>
    <div class="label__bottom-bar">
      <span class="label__line">EXKLUSIVE <strong>GASTRO GOURMET LINIE</strong></span>
    </div>
  </section>

  <section class="label label--naturelle">
    <div class="label__artwork" role="img" aria-label="Künstlerischer Hintergrund mit feinen, hellen Zweig- und Wasserlinien auf rotem Verlauf"></div>
    <div class="label__top-bar"></div>
    <div class="label__brand">mirel</div>
    <div class="label__variant">NATURELLE</div>
    <p class="label__description">Natürliches Mineralwasser ohne Kohlensäure</p>
    <div class="label__bottom-bar">
      <span class="label__line">EXKLUSIVE <strong>GASTRO GOURMET LINIE</strong></span>
    </div>
  </section>
</main>
</body>
</html>
```